Canadian furniture distributor

I need a logo design for my new company, Bright Oak G.P., Ergonomic High-End furniture distribution (very attractive patented design -mainly Desks & Chairs-).

Can be used for children adults, elders or limited mobility people.

Colors and design should match logo colors and products.

Industry/Entity Type

It Company

```html
<!DOCTYPE html>
<html lang="en">
<head>
<meta charset="utf-8">
<title>Bright Oak – Business Card</title>
<link href="https://fonts.googleapis.com/css2?family=Quicksand:wght@500;600;700&display=swap" rel="stylesheet">
<style>
  :root{
    --bg:#3a3431;
    --card:#161616;
    --magenta:#b0266f;
    --yellow:#f6a91f;
    --white:#ffffff;
    --emboss:#4a4a4a;
    --photo-a:#e9eef2;
    --photo-b:#b9c3cc;
  }
  *{box-sizing:border-box;margin:0;padding:0}
  html,body{width:1200px;height:716px;overflow:hidden;background:var(--bg)}
  body{font-family:"Quicksand",sans-serif;position:relative}
  .card{position:absolute;top:203px;width:540px;height:310px;background:var(--card);overflow:hidden;border-radius:2px;box-shadow:0 10px 30px rgba(0,0,0,.45)}
  .card--front{left:40px}
  .card--back{left:620px}

  /* front */
  .front-brand{position:absolute;left:34px;top:58px;display:flex;align-items:center;gap:10px;font-weight:700;font-size:28px;color:var(--emboss)}
  .front-brand .mark{width:20px;height:20px;background:var(--emboss)}
  .product-photo{position:absolute;left:280px;top:26px;width:228px;height:160px;border-radius:4px;background:linear-gradient(160deg,var(--photo-a),var(--photo-b))}
  .front-rule{position:absolute;left:0;right:0}
  .front-rule--yellow{top:202px;height:3px;background:var(--yellow)}
  .front-rule--magenta{top:212px;height:6px;background:var(--magenta)}
  .front-web{position:absolute;left:34px;top:240px;font-weight:700;font-size:17px;letter-spacing:.5px;color:var(--yellow)}

  /* back */
  .back-bands{position:absolute;inset:0}
  .back-brand{position:absolute;left:0;right:0;top:40px;display:flex;justify-content:center;align-items:center;gap:10px;font-weight:700;font-size:28px;color:var(--magenta)}
  .back-brand .mark{width:20px;height:20px;background:var(--magenta)}
  .address{position:absolute;left:30px;top:162px;font-weight:700;font-size:13px;line-height:19px;color:var(--white)}
  .person-name{position:absolute;right:30px;top:128px;font-weight:700;font-size:15px;letter-spacing:.6px;color:var(--magenta)}
  .person-title{position:absolute;right:30px;top:155px;font-weight:600;font-size:12px;color:var(--white)}
  .contacts{position:absolute;right:30px;top:176px;list-style:none}
  .contacts li{display:flex;justify-content:flex-end;align-items:center;gap:8px;font-weight:700;font-size:14px;line-height:21px;color:var(--white)}
  .contacts svg{width:13px;height:13px;flex:none}
</style>
</head>
<body>

<section class="card card--front">
  <div class="front-brand"><span class="mark"></span>Bright Oak</div>
  <div class="product-photo" role="img" aria-label="Photo of a white ergonomic height-adjustable desk"></div>
  <div class="front-rule front-rule--yellow"></div>
  <div class="front-rule front-rule--magenta"></div>
  <div class="front-web">www.brightoakdesk.com</div>
</section>

<section class="card card--back">
  <svg class="back-bands" viewBox="0 0 540 310" aria-hidden="true">
    <line x1="40" y1="150" x2="510" y2="150" stroke="var(--magenta)" stroke-width="1.5"/>
    <path d="M0 214 H236 Q262 214 278 228 H0 Z" fill="var(--yellow)"/>
    <path d="M0 236 H250 C280 236 290 290 330 290 H540 V310 H0 Z" fill="var(--magenta)"/>
  </svg>
  <div class="back-brand"><span class="mark"></span>Bright Oak</div>
  <div class="address">2418 Maple Ridge Rd Suite 210,<br>Ottawa ON K2P 1L4</div>
  <div class="person-name">EMPLOYEE NAME</div>
  <div class="person-title">Title</div>
  <ul class="contacts">
    <li>800.555.0142
      <svg viewBox="0 0 13 13"><rect width="13" height="13" rx="2" fill="var(--yellow)"/><path d="M4 3 L5.5 3 L6 5 L5 6 Q6 8 7.5 8.5 L8.5 7.5 L10 8 V9.5 Q6 10 3.5 5 Z" fill="var(--card)"/></svg></li>
    <li>800.555.0187
      <svg viewBox="0 0 13 13"><rect width="13" height="13" rx="2" fill="var(--yellow)"/><rect x="4" y="2.5" width="5" height="3" fill="var(--card)"/><rect x="2.5" y="6" width="8" height="4.5" fill="var(--card)"/></svg></li>
    <li>info@brightoakdesk.com
      <svg viewBox="0 0 13 13"><rect width="13" height="13" rx="2" fill="var(--yellow)"/><rect x="2.5" y="3.5" width="8" height="6" fill="none" stroke="var(--card)" stroke-width="1"/><path d="M2.5 3.5 L6.5 7 L10.5 3.5" fill="none" stroke="var(--card)" stroke-width="1"/></svg></li>
    <li>www.brightoakdesk.com
      <svg viewBox="0 0 13 13"><circle cx="6.5" cy="6.5" r="6" fill="var(--yellow)"/><circle cx="6.5" cy="6.5" r="4" fill="none" stroke="var(--card)" stroke-width=".9"/><ellipse cx="6.5" cy="6.5" rx="1.8" ry="4" fill="none" stroke="var(--card)" stroke-width=".9"/><line x1="2.5" y1="6.5" x2="10.5" y2="6.5" stroke="var(--card)" stroke-width=".9"/></svg></li>
  </ul>
</section>

</body>
</html>
```